Create a premium soap bar box bar design for an all-natural, men's skincare brand.

We are launching a men’s premium, natural soap bar and skincare business. To start, we will be launching cold-press, all-natural soap bars with a few additional products such as lotions. We plan to expand our line into additional skincare products such as face exfoliants, moisturizers and cleansers that target basic needs such as anti-aging, clarifying and hydrating.

Our target audience is men ages 25-50, with a secondary audience of male teens. Our target audience are mid to high income, professionals that live in more urban areas, but enjoy being active outdoors after work and on the weekends. Our target audience are hard workers, humble and want to enjoy all that life has to offer – whether that’s on top of a mountain or an ocean wave. They hike, bike, skateboard, surf or any other sport that gets them outside. They are husbands, brothers and fathers – there for their family and friends.

Our brand is sophisticated, adventurous and has a sense of humor. Many of our competitors either focus on the rugged outdoors or are more pretentious. We are in-between. We are free spirited and love the fresh air. Our products are trustworthy with no toxic chemicals or harsh ingredients. We are all-natural and provide high-quality, premium products that our audience expects and deserves.

Target Market(s)

Men, ages 25-54 who are high-earning professionals, yet enjoy getting outdoors and being active on the weekends - hiking, biking, surfing, skateboarding and more.

Industry/Entity Type

Men's skincare

Font styles to use
Sans Serif

Requirements
Must have
• See attachments
Nice to have
• We would prefer to a have a premium, slightly more modern looking design that will appeal to our target audience and slightly higher price point.
Should not have
• Please do not include an icon for the fragrance, i.e. cinnamon sticks. However, we do need some differentiation for the fragrance, i.e. color, etc. as it will be on the shelf with other fragrances.

```html
<!DOCTYPE html>
<html lang="en">
<head>
<meta charset="utf-8">
<title>Hale Fellow – Cinnamon Bark Soap Box</title>
<link rel="stylesheet" href="https://fonts.googleapis.com/css2?family=Jost:wght@400;500;600;700&family=Montserrat:wght@400;600;700&display=swap">
<style>
  :root {
    --backdrop: #f3f3f3;
    --signal-red: #e94545;
    --signal-red-deep: #c93a3a;
    --kraft: #c49a6c;
    --navy: #10263f;
    --navy-light: #1b3b58;
    --white: #ffffff;
  }
  * { margin: 0; padding: 0; box-sizing: border-box; }
  html, body { width: 1200px; height: 675px; overflow: hidden; background: var(--backdrop); }
  .canvas { position: relative; width: 1200px; height: 675px; }

  .front-panel {
    position: absolute; left: 250px; top: 105px; width: 560px; height: 465px;
    background: var(--kraft); overflow: hidden;
    font-family: "Jost", sans-serif;
  }
  .top-band {
    position: absolute; left: 0; top: 0; width: 100%; height: 100px;
    background: var(--signal-red);
    display: flex; align-items: center; justify-content: center;
  }
  .category-line {
    color: var(--white); font-weight: 700; font-size: 27px; letter-spacing: 0.2em;
  }
  .brand-lockup {
    position: absolute; top: 135px; left: 0; width: 100%;
    display: flex; align-items: center; justify-content: center; gap: 16px;
  }
  .brand-dot {
    width: 54px; height: 54px; border-radius: 50%; border: 3px solid var(--navy);
  }
  .brand-text { display: flex; flex-direction: column; }
  .brand-name {
    color: var(--navy); font-weight: 500; font-size: 46px; letter-spacing: 0.06em; line-height: 1;
  }
  .brand-tagline {
    color: var(--signal-red); font-weight: 400; font-size: 13px; letter-spacing: 0.55em; margin-top: 4px;
  }
  .scent-block { position: absolute; top: 232px; left: 0; width: 100%; text-align: center; }
  .scent-name { color: var(--navy); font-weight: 700; font-size: 38px; letter-spacing: 0.03em; line-height: 1; }
  .scent-notes { color: var(--signal-red); font-size: 14px; letter-spacing: 0.5em; margin-top: 6px; }
  .mountain-band {
    position: absolute; left: 0; bottom: 0; width: 100%; height: 145px;
    background: linear-gradient(180deg, var(--navy-light) 0%, var(--navy) 60%);
  }
  .net-weight {
    position: absolute; left: 0; bottom: 38px; width: 100%; text-align: center;
    color: var(--white); font-weight: 600; font-size: 20px; z-index: 1;
  }

  .side-panel {
    position: absolute; left: 818px; top: 105px; width: 130px; height: 465px;
    background: var(--navy); overflow: hidden;
    font-family: "Montserrat", sans-serif;
  }
  .side-top-band { position: absolute; left: 0; top: 0; width: 100%; height: 100px; background: var(--signal-red-deep); }
  .side-copy {
    position: absolute; left: 50%; top: 290px; width: 340px;
    transform: translate(-50%, -50%) rotate(-90deg);
    color: var(--white);
  }
  .side-invite { font-size: 15px; font-weight: 400; }
  .side-url { font-size: 34px; font-weight: 700; line-height: 1.05; }
  .directions { display: flex; align-items: stretch; margin-top: 8px; font-size: 10px; }
  .directions-label { background: var(--white); color: var(--navy); font-weight: 700; padding: 4px 8px; }
  .directions-text { border: 1px solid var(--white); padding: 4px 10px; flex: 1; }
</style>
</head>
<body>
<div class="canvas">
  <section class="front-panel">
    <div class="top-band"><p class="category-line">MEN’S NATURAL SOAP</p></div>
    <div class="brand-lockup">
      <span class="brand-dot"></span>
      <div class="brand-text">
        <p class="brand-name">HALE FELLOW</p>
        <p class="brand-tagline">REAL SKINCARE</p>
      </div>
    </div>
    <div class="scent-block">
      <p class="scent-name">CINNAMON BARK</p>
      <p class="scent-notes">SWEET &amp; SPICY</p>
    </div>
    <div class="mountain-band" role="img" aria-label="Navy mountain range silhouette"></div>
    <p class="net-weight">5 Oz. Bar</p>
  </section>

  <aside class="side-panel">
    <div class="side-top-band"></div>
    <div class="side-copy">
      <p class="side-invite">Check out all our products at</p>
      <p class="side-url">halefellow.com</p>
      <div class="directions">
        <span class="directions-label">DIRECTIONS:</span>
        <span class="directions-text">Lather, rinse and repeat.</span>
      </div>
    </div>
  </aside>
</div>
</body>
</html>
```